Strength and Movement Coaching for Every Day
Project: Business Card & Letterhead
Business Card & Letterhead
Bright & Fun-filled
Dale Varnek
Strength & Conditioning Coach
42 Millbrook Lane Harrowfield, VT 05742
dale@strideformlab.com
www.strideformlab.com
Whether competing on the field of play or in the game of life Stride Form Lab is your proven partner for: Performance Enhancement Injury Reduction & Rehabilitation Weight Management & Nutritional Strategies General Fitness Consulting to Companies and Schools Team Training

```html
<!DOCTYPE html>
<html lang="en">
<head>
<meta charset="utf-8">
<title>Stride Form Lab – Business Card</title>
<link rel="stylesheet" href="https://fonts.googleapis.com/css2?family=Open+Sans:ital,wght@0,400;0,600;0,700;1,400;1,600&display=swap">
<style>
  :root {
    --blue: #1d5fc4;
    --blue-deep: #0f47a8;
    --blue-light: #3b82e6;
    --sky: #6aa6f0;
    --ink: #444b55;
    --white: #ffffff;
    --backdrop: #eceef1;
  }
  * { box-sizing: border-box; margin: 0; padding: 0; }
  html, body { width: 1200px; height: 980px; overflow: hidden; }
  body {
    background: var(--backdrop);
    font-family: "Open Sans", sans-serif;
    position: relative;
  }
  .card {
    position: absolute;
    width: 700px;
    height: 400px;
    border-radius: 22px;
    overflow: hidden;
    box-shadow: 0 10px 30px rgba(0,0,0,0.15);
  }
  /* Back side */
  .card-back {
    left: 440px; top: 70px;
    background: linear-gradient(135deg, var(--blue-light) 0%, var(--blue) 45%, var(--blue-deep) 100%);
    color: var(--white);
  }
  .back-copy {
    position: absolute;
    left: 300px; top: 78px; right: 36px;
  }
  .back-intro {
    font-size: 15px;
    font-weight: 600;
    font-style: italic;
    line-height: 1.45;
    margin-bottom: 14px;
  }
  .service-list { list-style: none; }
  .service-list li {
    font-size: 14px;
    line-height: 1.75;
    display: flex;
    align-items: center;
    gap: 10px;
  }
  .service-list li::before {
    content: "";
    width: 9px; height: 9px;
    border-radius: 50%;
    background: var(--white);
    flex: none;
  }
  /* Front side */
  .card-front {
    left: 60px; top: 510px;
    background: var(--white);
  }
  .front-swoosh { position: absolute; inset: 0; }
  .brand {
    position: absolute;
    left: 44px; top: 46px;
  }
  .brand-name {
    display: flex;
    align-items: center;
    gap: 14px;
    font-size: 38px;
    font-weight: 600;
    color: var(--blue);
    letter-spacing: -0.5px;
  }
  .brand-dot {
    width: 30px; height: 30px;
    border-radius: 50%;
    background: var(--blue);
  }
  .brand-tagline {
    margin-top: 4px;
    margin-left: 44px;
    font-size: 16px;
    font-style: italic;
    color: var(--blue-light);
  }
  .contact-list {
    position: absolute;
    left: 44px; top: 166px;
    list-style: none;
  }
  .contact-list li {
    display: flex;
    align-items: flex-start;
    gap: 10px;
    font-size: 13.5px;
    color: var(--ink);
    line-height: 1.35;
    margin-bottom: 8px;
  }
  .contact-icon { width: 18px; height: 18px; flex: none; margin-top: 1px; }
  .person {
    position: absolute;
    left: 300px; top: 308px;
    width: 230px;
    text-align: right;
  }
  .person-name {
    font-size: 17px;
    font-weight: 700;
    color: var(--blue);
  }
  .person-title {
    font-size: 13px;
    font-style: italic;
    color: var(--ink);
  }
</style>
</head>
<body>

<section class="card card-back" aria-label="Card back">
  <div class="back-copy">
    <p class="back-intro">Whether competing on the field of play or in the game of life Stride Form Lab is your proven partner for:</p>
    <ul class="service-list">
      <li>Performance Enhancement</li>
      <li>Injury Reduction &amp; Rehabilitation</li>
      <li>Weight Management &amp; Nutritional Strategies</li>
      <li>General Fitness</li>
      <li>Consulting to Companies and Schools</li>
      <li>Team Training</li>
    </ul>
  </div>
</section>

<section class="card card-front" aria-label="Card front">
  <svg class="front-swoosh" viewBox="0 0 700 400" preserveAspectRatio="none" aria-hidden="true">
    <path d="M700 60 C 640 200, 560 320, 420 400 L 700 400 Z" fill="var(--sky)" opacity="0.55"/>
    <path d="M700 95 C 655 220, 590 330, 480 400 L 700 400 Z" fill="var(--white)"/>
    <path d="M700 120 C 665 235, 610 335, 520 400 L 700 400 Z" fill="var(--blue)"/>
    <path d="M700 150 C 675 250, 630 340, 565 400 L 700 400 Z" fill="var(--blue-deep)"/>
  </svg>

  <div class="brand">
    <div class="brand-name"><span class="brand-dot"></span>Stride Form Lab</div>
    <p class="brand-tagline">Strength and Movement Coaching for Every Day</p>
  </div>

  <ul class="contact-list">
    <li>
      <svg class="contact-icon" viewBox="0 0 18 18" aria-hidden="true"><circle cx="9" cy="9" r="9" fill="var(--blue)"/><path d="M9 4a3 3 0 0 0-3 3c0 2.3 3 6 3 6s3-3.7 3-6a3 3 0 0 0-3-3zm0 4.2a1.2 1.2 0 1 1 0-2.4 1.2 1.2 0 0 1 0 2.4z" fill="var(--white)"/></svg>
      <span>42 Millbrook Lane<br>Harrowfield, VT 05742</span>
    </li>
    <li>
      <svg class="contact-icon" viewBox="0 0 18 18" aria-hidden="true"><circle cx="9" cy="9" r="9" fill="var(--blue)"/><path d="M6.2 4.5l1.6 1.8-.9 1.3c.6 1.3 1.5 2.2 2.8 2.8l1.3-.9 1.8 1.6-.9 1.6c-3.4-.3-6.3-3.2-6.6-6.6z" fill="var(--white)"/></svg>
      <span>802 555 0142</span>
    </li>
    <li>
      <svg class="contact-icon" viewBox="0 0 18 18" aria-hidden="true"><circle cx="9" cy="9" r="9" fill="var(--blue)"/><rect x="4.5" y="6" width="9" height="6.5" rx="1" fill="var(--white)"/><path d="M4.8 6.3L9 9.4l4.2-3.1" stroke="var(--blue)" stroke-width="0.9" fill="none"/></svg>
      <span>dale@strideformlab.com</span>
    </li>
    <li>
      <svg class="contact-icon" viewBox="0 0 18 18" aria-hidden="true"><circle cx="9" cy="9" r="9" fill="var(--blue)"/><circle cx="9" cy="9" r="4.3" fill="none" stroke="var(--white)" stroke-width="1"/><path d="M4.7 9h8.6M9 4.7c-2 2.4-2 6.2 0 8.6M9 4.7c2 2.4 2 6.2 0 8.6" stroke="var(--white)" stroke-width="0.9" fill="none"/></svg>
      <span>www.strideformlab.com</span>
    </li>
  </ul>

  <div class="person">
    <p class="person-name">Dale Varnek</p>
    <p class="person-title">Strength &amp; Conditioning Coach</p>
  </div>
</section>

</body>
</html>
```